Print & Packaging Design for Wee Fern Teething & Healing Necklaces

Bring your Creative Juices this-a way! Smart, savvy, up-market business needs a logo & swing tags! Do you have what it takes?

```html
<!DOCTYPE html>
<html lang="en">
<head>
<meta charset="utf-8">
<title>Wee Fern Teething &amp; Healing Necklaces – Swing Tags</title>
<link href="https://fonts.googleapis.com/css2?family=Delius&display=swap" rel="stylesheet">
<style>
  :root {
    --page: #ffffff;
    --lilac-deep: #9c8fcf;
    --lilac-mid: #b3a8dc;
    --lilac-soft: #cbc3ea;
    --lilac-light: #e3def4;
    --plum: #86489f;
    --violet-text: #6f479f;
    --tag-copy: #ffffff;
    --copy-shade: rgba(70, 48, 130, 0.55);
    --photo-warm: #e9d9cf;
    --photo-cool: #c9d3ea;
    --string: #2f2f3a;
    --hole-ring: #3a3a44;
  }
  html, body {
    margin: 0;
    padding: 0;
    width: 1200px;
    height: 749px;
    overflow: hidden;
    background: var(--page);
  }
  .canvas {
    position: relative;
    width: 1200px;
    height: 749px;
    overflow: hidden;
    font-family: "Delius", "Trebuchet MS", sans-serif;
  }
  .swing-tag {
    position: absolute;
    overflow: hidden;
    border-radius: 95px 0 170px 0 / 135px 0 200px 0;
  }
  .swing-tag--front {
    left: 107px; top: 0; width: 913px; height: 363px;
    background:
      radial-gradient(ellipse at 62% 48%, var(--lilac-light) 0%, rgba(227,222,244,0) 55%),
      linear-gradient(100deg, var(--lilac-soft) 0%, var(--lilac-mid) 55%, var(--lilac-deep) 100%);
  }
  .swing-tag--back {
    left: 291px; top: 380px; width: 909px; height: 369px;
    background:
      linear-gradient(100deg, var(--lilac-soft) 0%, var(--lilac-mid) 40%, var(--lilac-deep) 100%);
  }

  .tag-photo {
    position: absolute;
    left: 0;
    top: 0;
    height: 100%;
    width: 310px;
    background:
      linear-gradient(90deg, rgba(255,255,255,0) 72%, var(--lilac-soft) 100%),
      radial-gradient(ellipse at 45% 55%, var(--photo-warm) 0%, #f4eee9 45%, var(--photo-cool) 100%);
  }
  .swing-tag--back .tag-photo { width: 300px; }

  .brand {
    position: absolute;
    left: 300px;
    top: 118px;
    width: 560px;
    text-align: center;
  }
  .brand-name {
    display: flex;
    align-items: center;
    justify-content: center;
    gap: 16px;
    margin: 0;
    font-size: 70px;
    font-weight: 400;
    line-height: 1;
    color: var(--plum);
  }
  .brand-dot {
    width: 18px;
    height: 18px;
    border-radius: 50%;
    background: var(--plum);
  }
  .brand-tagline {
    margin: 22px 0 0;
    font-size: 24px;
    color: var(--violet-text);
  }

  .tag-copy {
    position: absolute;
    left: 330px;
    top: 70px;
    margin: 0;
    padding: 0;
    list-style: none;
    font-size: 20px;
    line-height: 31px;
    color: var(--tag-copy);
    letter-spacing: 0.2px;
    text-shadow: 0 1px 2px var(--copy-shade);
  }

  .tag-string {
    position: absolute;
    left: 0;
    top: 0;
    pointer-events: none;
  }
</style>
</head>
<body>
<main class="canvas">

  <section class="swing-tag swing-tag--front" aria-label="Swing tag front">
    <div class="tag-photo" role="img" aria-label="Photo of a mother gently cuddling her sleeping newborn"></div>
    <div class="brand">
      <h1 class="brand-name"><span class="brand-dot"></span>Wee Fern</h1>
      <p class="brand-tagline">Teething &amp; Healing Necklaces</p>
    </div>
  </section>

  <section class="swing-tag swing-tag--back" aria-label="Swing tag back">
    <div class="tag-photo" role="img" aria-label="Photo of a mother gently cuddling her sleeping newborn"></div>
    <ul class="tag-copy">
      <li>"natural pain relief for your babe"</li>
      <li>"relieve your babes pain and sleep better at night"</li>
      <li>"sleep better at night knowing you've helped</li>
      <li>to ease your babes pain"</li>
      <li>"baltic amber teething necklaces"</li>
      <li>"gemstone nursing necklaces"</li>
      <li>"fertility and birthing jewellery"</li>
      <li>"natural healing jewellery"</li>
    </ul>
  </section>

  <svg class="tag-string" width="1200" height="749" viewBox="0 0 1200 749" aria-hidden="true">
    <g fill="none" stroke="var(--string)" stroke-width="3.5" stroke-linecap="round">
      <path d="M150 302 C110 290, 60 286, 18 292"/>
      <path d="M150 308 C105 322, 50 330, 0 340"/>
      <path d="M331 686 C290 674, 240 670, 200 676"/>
      <path d="M331 692 C285 706, 230 716, 182 726"/>
    </g>
    <g fill="#ffffff" stroke="var(--hole-ring)" stroke-width="2">
      <circle cx="163" cy="304" r="13"/>
      <circle cx="344" cy="688" r="13"/>
    </g>
  </svg>

</main>
</body>
</html>
```